I am looking for business cards and letterhead

I want a high-level look for CEO's who want a concierge level leadership consultant and organization development strategist

This needs to go with my brand: simple, elegant, clean. Please improve on this design while using these fonts and colors

Here is my website: CorinneValdez.com

```html
<!DOCTYPE html>
<html lang="en">
<head>
<meta charset="utf-8">
<title>Corinne Valdez — Business Card</title>
<link rel="stylesheet" href="https://fonts.googleapis.com/css2?family=Montserrat:wght@400;500;700&display=swap">
<style>
  :root {
    --navy: #0b1535;
    --gold: #c2a56e;
    --gold-deep: #b8954f;
    --white: #ffffff;
    --backdrop: #ececec;
  }
  html, body {
    margin: 0;
    width: 1200px;
    height: 1200px;
    overflow: hidden;
    background: var(--backdrop);
    font-family: "Montserrat", Arial, sans-serif;
  }
  .sheet {
    position: relative;
    width: 1200px;
    height: 1200px;
  }
  .card {
    position: absolute;
    left: 178px;
    width: 845px;
    height: 495px;
    display: block;
  }
  .card--front { top: 81px; }
  .card--back { top: 616px; }
  .card-name {
    font-weight: 700;
    font-size: 28px;
    fill: var(--gold);
    letter-spacing: 0.5px;
  }
  .contact-text {
    font-weight: 400;
    font-size: 17px;
    fill: var(--white);
  }
  .contact-icon { fill: var(--gold); }
  .brand-name {
    font-weight: 500;
    fill: var(--gold-deep);
    letter-spacing: 1px;
  }
</style>
</head>
<body>
<main class="sheet">

  <svg class="card card--front" viewBox="0 0 676 396" role="group" aria-label="Business card front">
    <defs>
      <clipPath id="front-clip"><rect width="676" height="396"/></clipPath>
    </defs>
    <g clip-path="url(#front-clip)">
      <rect class="front-field" width="676" height="396" fill="var(--navy)"/>
      <circle class="front-arc" cx="700" cy="-24" r="358" fill="var(--white)" stroke="var(--gold)" stroke-width="5"/>
    </g>

    <g class="front-brand">
      <circle cx="533" cy="106" r="7" fill="var(--gold-deep)"/>
      <text class="brand-name" x="533" y="146" text-anchor="middle" font-size="20">Corinne Valdez</text>
    </g>

    <text class="card-name" x="40" y="216">YOUR NAME</text>

    <g class="contact-list">
      <g class="contact-row">
        <path class="contact-icon" d="M41 266c1-1 2-1 3 0l2 2c1 1 1 2 0 3l-1 1c1 2 3 4 5 5l1-1c1-1 2-1 3 0l2 2c1 1 1 2 0 3l-1 1c-2 2-6 0-10-4s-6-8-4-10z"/>
        <text class="contact-text" x="66" y="278">(512) 555 0148</text>
      </g>
      <g class="contact-row">
        <rect class="contact-icon" x="40" y="298" width="14" height="10" rx="1"/>
        <path d="M40 299l7 5 7-5" fill="none" stroke="var(--navy)" stroke-width="1.3"/>
        <text class="contact-text" x="66" y="309">info@CorinneValdez.com</text>
      </g>
      <g class="contact-row">
        <circle cx="47" cy="334" r="6.5" fill="none" stroke="var(--gold)" stroke-width="1.6"/>
        <path d="M40.5 334h13M47 327.5c-3 4-3 9 0 13M47 327.5c3 4 3 9 0 13" fill="none" stroke="var(--gold)" stroke-width="1.2"/>
        <text class="contact-text" x="66" y="340">www.CorinneValdez.com</text>
      </g>
    </g>
  </svg>

  <svg class="card card--back" viewBox="0 0 676 396" role="group" aria-label="Business card back">
    <rect class="back-field" width="676" height="396" fill="var(--white)"/>
    <path class="back-sweep-navy" d="M330 346 C450 330 580 318 676 300 L676 336 C560 352 450 354 330 346 Z" fill="var(--navy)"/>
    <path class="back-sweep-gold" d="M0 195 C70 300 200 344 318 346 C330 346 335 343 345 343 C460 350 580 345 676 335 L676 396 L0 396 Z" fill="var(--gold)"/>

    <g class="back-brand">
      <circle cx="333" cy="160" r="9" fill="var(--gold-deep)"/>
      <text class="brand-name" x="333" y="212" text-anchor="middle" font-size="28">Corinne Valdez</text>
    </g>
  </svg>

</main>
</body>
</html>
```